Green blog

Hi there !
I want to redesign my french green blog here: http://www.verdanimo.info

I want the same presentation, but something much funny, professionnal and great !

I have a new logo to integrate it, i'll put it on the attachment.

Thank you so much for your work in advance !

Hello there !

The price is for only the design, not the wordpress integration !

Thanks

```html
<!DOCTYPE html>
<html lang="fr">
<head>
<meta charset="utf-8">
<title>Verdanimo</title>
<link rel="stylesheet" href="https://fonts.googleapis.com/css2?family=Arimo:wght@400;700&display=swap">
<style>
:root{
  --sky-top:#6fb6ea;
  --sky-mid:#bfe2f7;
  --sky-low:#eef8fd;
  --frame:#3d8c35;
  --lime:#7bb521;
  --tab:#4aa547;
  --title:#69a81c;
  --text:#333333;
  --muted:#555555;
  --line:#3d8c35;
  --white:#ffffff;
  --field:#ececec;
}
*{box-sizing:border-box;margin:0;padding:0}
html,body{width:904px;height:1200px;overflow:hidden}
body{
  position:relative;
  font-family:"Arimo",Arial,sans-serif;
  color:var(--text);
  background:linear-gradient(180deg,var(--sky-top) 0,var(--sky-mid) 180px,var(--sky-low) 420px,#ffffff 700px,#ffffff 100%);
}
.abs{position:absolute}
.header-scene{left:103px;top:80px;width:700px;height:140px;
  background:linear-gradient(180deg,rgba(185,221,74,0) 0,#b9dd4a 30%,#8cc63f 65%,#4f9d2f 100%)}
.footer-scene{left:0;top:1040px;width:904px;height:160px;
  background:linear-gradient(180deg,rgba(243,247,176,0) 0,#e6f07a 25%,#b9dc3c 60%,#7cc02c 100%)}
.logo{left:107px;top:30px;display:flex;align-items:center;gap:8px}
.logo-mark{width:52px;height:52px;border-radius:50%;background:#5a9bd4}
.logo-name{font-size:30px;font-weight:400;color:#e0d92a;letter-spacing:1px}
.frame{left:103px;top:220px;width:700px;height:800px;background:var(--frame)}
.card{position:absolute;left:115px;width:406px;background:var(--white);padding:0 13px}
.post-title{font-size:14.5px;font-weight:700;color:var(--title);margin-top:14px;padding-right:50px}
.post-meta{font-size:9px;color:var(--muted);margin-top:8px}
.post-meta em{font-style:italic}
.post-meta b{color:var(--text)}
.post p{font-size:9.3px;line-height:13.5px;margin-top:6px;padding-right:4px}
.post p.lead{margin-top:22px}
.tweet{position:absolute;right:13px;top:16px;text-align:center;width:35px}
.tweet-count{width:35px;height:31px;border:1px solid #d0d0d0;background:#f4f4f4;font-size:11px;font-weight:700;line-height:13px;padding-top:4px}
.tweet-count small{display:block;font-size:7px;font-weight:400;color:var(--muted)}
.retweet{margin-top:4px;background:#a4cf5c;color:#fff;font-size:7px;padding:1px 0;border-radius:2px}
.video{position:relative;width:340px;height:253px;margin:16px auto 0;background:#111}
.video-picture{position:absolute;left:0;top:30px;width:340px;height:175px;background:linear-gradient(180deg,#6fa4b3 0,#4f8592 60%,#2b4a55 100%)}
.video-bar{position:absolute;left:0;bottom:0;width:340px;height:48px;background:#1a1a1a}
.play{position:absolute;left:6px;bottom:5px;width:46px;height:40px;background:#000;border:1px solid #444}
.play svg{position:absolute;left:15px;top:12px}
.video-title{position:absolute;left:58px;bottom:30px;color:#fff;font-size:12px;font-weight:700}
.video-by{position:absolute;left:58px;bottom:16px;color:#ccc;font-size:8px}
.video-time{position:absolute;left:58px;bottom:4px;color:#ccc;font-size:7px}
.video-brand{position:absolute;right:8px;bottom:8px;color:#ddd;font-size:11px}
.post-foot{position:relative;font-size:9px;margin-top:18px;line-height:16px}
.post-foot b{color:var(--text)}
.post-foot span{color:var(--lime);font-weight:700}
.read-more{position:absolute;right:0;bottom:0;background:var(--lime);color:#fff;font-size:8.5px;font-weight:700;padding:2px 8px}
.pager{top:969px;height:26px;background:var(--lime);color:#fff;font-size:11px;font-weight:700;display:flex;align-items:center;gap:8px;padding:0 12px}
.side-box{position:absolute;left:535px;width:254px;background:var(--white)}
.search{top:233px;height:40px;padding:8px 13px;display:flex;align-items:center;gap:8px}
.search-field{width:196px;height:24px;background:var(--field);border:1px solid #cfcfcf;font-size:13px;color:#444;padding:3px 6px}
.box-title{font-size:15.5px;color:var(--title);padding:12px 13px 8px}
.list{list-style:none;padding:0 13px}
.list li{font-size:10px;line-height:25px;border-bottom:1px solid var(--line)}
.list li:last-child{border-bottom:none}
.tabs{display:flex;height:33px}
.tab{flex:1;font-size:13.5px;display:flex;align-items:center;justify-content:center}
.tab.active{background:#fff;color:#222}
.tab.off{background:var(--tab);color:#fff}
.tabs-list li{padding-left:12px;line-height:26px}
.follow{left:535px;top:706px;color:#fff;display:flex;align-items:baseline;gap:8px}
.follow-small{font-size:13.5px;font-weight:700}
.follow-name{font-size:30px;font-weight:700}
.duo{top:776px;height:179px;display:flex}
.duo-col{flex:1;border-right:1px solid var(--line)}
.duo-col:last-child{border-right:none}
.duo-head{height:67px;background:var(--tab);color:#fff;font-size:12px;text-align:center;display:flex;align-items:center;justify-content:center;line-height:15px;padding:0 8px}
.badge{width:58px;height:58px;border-radius:50%;border:3px solid #4a9d35;margin:24px auto 0}
</style>
</head>
<body>
  <div class="abs header-scene" role="img" aria-label="Illustration of green hills with small houses, trees and flowers"></div>
  <div class="abs footer-scene" role="img" aria-label="Illustration of rolling yellow-green meadows with sparkles"></div>

  <div class="abs logo">
    <div class="logo-mark"></div>
    <div class="logo-name">Verdanimo</div>
  </div>

  <div class="abs frame"></div>

  <article class="card post" style="top:233px;height:440px">
    <h2 class="post-title">Vivez, prospérez, consommez</h2>
    <div class="post-meta"><em>juillet 7th, 2010</em> &nbsp;| &nbsp;<b>by Lucas</b></div>
    <div class="tweet"><div class="tweet-count">5<small>tweets</small></div><div class="retweet">retweet</div></div>
    <p class="lead">Un documentaire qui fait vraiment réfléchir sur notre façon de vivre et de consommer sans limite! 3 vidéos à voir sans modération pour mieux comprendre le cercle vicieux dans lequel nous sommes depuis la révolution industrielle du siècle dernier.</p>
    <div class="video">
      <div class="video-picture" role="img" aria-label="Video still from an animated documentary"></div>
      <div class="video-bar">
        <div class="play"><svg width="16" height="16" viewBox="0 0 16 16"><path d="M2 1 L14 8 L2 15 Z" fill="#fff"/></svg></div>
        <div class="video-title">Vivez, prospérez, consommez 1/3</div>
        <div class="video-by">By Sentierguide</div>
        <div class="video-time">18:22</div>
        <div class="video-brand">Vidéoline</div>
      </div>
    </div>
    <div class="post-foot">
      <div><b>Tags</b> &nbsp;<span>levure</span> , <span>linge</span> , <span>noix de lavage</span></div>
      <div><b>Commentaires</b> &nbsp;<span>5 commentaires</span></div>
      <div class="read-more">read more</div>
    </div>
  </article>

  <article class="card post" style="top:687px;height:266px">
    <h2 class="post-title">Astuce 6: Du linge blanc naturellement</h2>
    <div class="post-meta"><em>juillet 8th, 2010</em> &nbsp;| &nbsp;<b>by Hugo</b></div>
    <div class="tweet"><div class="tweet-count">5<small>tweets</small></div><div class="retweet">retweet</div></div>
    <p class="lead">On sait que les lessives classiques sont souvent très nocives pour l'eau et se retrouvent dans nos rivières et nos océans, avec les désastres que l'on connait.</p>
    <p>C'est pour cette raison qu'il faut préférer une lessive écologique ou encore les fameuses noix de lavage.</p>
    <p>L'inconvénient avec ces noix, c'est que le linge devient parfois grisâtre, voici une solution proposée par Hugo.</p>
    <p>Pour éviter le linge grisâtre avec les noix de lavage, il suffit de mettre un sachet de levure chimique dans le tambour de la machine.</p>
    <div class="post-foot" style="margin-top:12px">
      <div><b>Tags</b> &nbsp;<span>levure</span> , <span>linge</span> , <span>noix de lavage</span></div>
      <div><b>Commentaires</b> &nbsp;<span>5 commentaires</span></div>
      <div class="read-more">read more</div>
    </div>
  </article>

  <div class="abs pager" style="left:115px">
    <svg width="9" height="10" viewBox="0 0 9 10"><path d="M8 0 L0 5 L8 10 Z" fill="#fff"/></svg>
    Articles précédents
  </div>
  <div class="abs pager" style="left:404px">
    Page suivante
    <svg width="9" height="10" viewBox="0 0 9 10"><path d="M1 0 L9 5 L1 10 Z" fill="#fff"/></svg>
  </div>

  <div class="side-box search">
    <div class="search-field">search here...</div>
    <svg width="22" height="22" viewBox="0 0 22 22"><circle cx="9" cy="9" r="6" fill="none" stroke="#888" stroke-width="2.5"/><path d="M13.5 13.5 L20 20" stroke="#555" stroke-width="3.5" stroke-linecap="round"/></svg>
  </div>

  <section class="side-box" style="top:291px;height:182px">
    <h3 class="box-title">Articles Récents</h3>
    <ul class="list">
      <li>La crise ne doit pas faire oublier l'écologie</li>
      <li>La crise ne doit pas faire oublier l'écologie</li>
      <li>La crise ne doit pas faire oublier l'écologie</li>
      <li>La crise ne doit pas faire oublier l'écologie</li>
      <li>La crise ne doit pas faire oublier l'écologie</li>
    </ul>
  </section>

  <section class="side-box" style="top:493px;height:190px">
    <div class="tabs"><div class="tab active">Informations</div><div class="tab off">Liens</div></div>
    <ul class="list tabs-list" style="margin-top:4px">
      <li>A propos</li>
      <li>Covoiturage</li>
      <li>Devenez redacteur</li>
      <li>Du bio pour votre bebe</li>
      <li>Economie denergie</li>
    </ul>
  </section>

  <div class="abs follow"><span class="follow-small">Follow us on</span><span class="follow-name">Socialia</span></div>

  <section class="side-box duo">
    <div class="duo-col">
      <div class="duo-head">Je compense les émissions de CO2 du blog</div>
      <div class="badge"></div>
    </div>
    <div class="duo-col">
      <div class="duo-head">Partenaires</div>
    </div>
  </section>
</body>
</html>
```